Home page concept, possible logo colour change

There is no need to code a home page, we are just looking for concept ideas.
We have had a logo designed for a new company we are starting named Corvantek Aluminium Windows & Doors. We are manufacturing bullet resistant window frames. We have had logo designed, we like the concept of the design, but the current colours (black and red) may not be the best option, especially when designing the website home page, and how it interacts with the logo colours. I have also attached the first draft of the home page which we are not happy with. The overall design/navigation is good, we have issues with the darkened out primary image and also the amount of red on the page, it just doesn't feel right. As mentioned before we are happy to look at colour changes to the logo.
Number of Pages Required
1 page
Look and feel
Each slider illustrates characteristics of the customer's brand and the style your logo design should communicate.

```html
<!DOCTYPE html>
<html lang="en">
<head>
<meta charset="utf-8">
<title>Corvantek Aluminium Windows &amp; Doors</title>
<link href="https://fonts.googleapis.com/css2?family=Poppins:wght@300;400;500;600;700;800&display=swap" rel="stylesheet">
<style>
:root{
  --blue:#2f7de1;
  --ink:#1f2530;
  --text:#3c4350;
  --mist:#e9edf2;
  --white:#ffffff;
  --footer:#2b2c2e;
  --footer-deep:#1f2022;
}
*{margin:0;padding:0;box-sizing:border-box}
html,body{width:1200px;height:3377px;overflow:hidden}
body{font-family:'Poppins',sans-serif;color:var(--text);background:var(--mist);position:relative}
.abs{position:absolute}
.btn{position:absolute;background:var(--blue);color:var(--white);font-weight:700;font-size:14px;display:flex;align-items:center;justify-content:center;text-transform:uppercase}
/* header */
.site-header{left:0;top:0;width:1200px;height:95px;background:var(--mist)}
.brand{left:111px;top:22px;color:var(--ink);font-weight:700;display:flex;gap:8px;align-items:flex-start}
.brand-mark{width:14px;height:14px;background:var(--blue);margin-top:8px}
.brand-name{font-size:27px;line-height:30px}
.brand-tag{font-size:7px;line-height:9px;letter-spacing:.5px;text-transform:uppercase}
.header-rule{left:0;top:92px;width:350px;height:3px;background:var(--blue)}
.nav{top:0;height:95px;display:flex;align-items:center;font-size:15px;font-weight:600;color:var(--ink);text-transform:uppercase}
.nav-active{left:429px;top:0;width:112px;height:95px;background:var(--white);color:var(--blue);justify-content:center}
/* hero */
.hero-photo{left:543px;top:95px;width:657px;height:465px;background:linear-gradient(135deg,#6d6a66,#b9b6b0 45%,#8a8882 70%,#4d4a47)}
.thumb-strip{left:809px;top:465px;width:391px;height:95px;background:var(--white)}
.thumb{top:476px;width:84px;height:75px}
.hero-title{left:111px;top:190px;font-size:39px;font-weight:800;line-height:40px;color:var(--ink)}
.hero-title span{color:var(--blue)}
.hero-sub{left:111px;top:278px;font-size:26px;font-weight:400;color:var(--ink)}
.hero-copy{left:111px;top:333px;width:362px;font-size:15.5px;line-height:30px;text-align:justify}
.slide-no{font-size:15px;color:var(--ink);width:40px;text-align:center}
.slide-on{left:33px;top:305px;height:37px;background:var(--white);color:var(--blue);display:flex;align-items:center;justify-content:center;font-weight:600}
/* features */
.feature-band{left:0;top:712px;width:1200px;height:238px;background:var(--blue)}
.feature-frame{left:254px;top:642px;width:694px;height:217px;background:var(--blue);box-shadow:0 6px 18px rgba(0,0,0,.12)}
.feature{top:666px;width:204px;height:170px;background:var(--white);text-align:center;padding-top:12px}
.feature h3{color:var(--blue);font-size:14.5px;font-weight:600;line-height:17px;margin-top:4px;text-transform:uppercase}
.feature p{font-size:15px;line-height:20px;color:var(--text);margin-top:4px;padding:0 18px}
/* about */
.about{left:0;top:950px;width:1200px;height:597px;background:linear-gradient(160deg,#f3f5f8,#ffffff 50%,#eef1f5)}
.block{background:var(--blue)}
.about h2,.range h2{color:var(--blue);font-weight:800;font-size:38px}
.about-copy{left:590px;top:1140px;width:462px;font-size:15.5px;line-height:30px;text-align:justify}
/* range */
.range-card{width:295px}
.range-img{top:1759px;width:295px;height:265px}
.range-box{top:2048px;width:295px;height:126px;background:var(--white);text-align:center;box-shadow:0 4px 12px rgba(0,0,0,.06)}
.range-box h3{color:var(--blue);font-size:19px;font-weight:600;margin-top:22px}
.range-box p{font-size:15.5px;line-height:27px}
/* enquiry */
.enquiry{left:0;top:2320px;width:1200px;height:722px;background:linear-gradient(120deg,#8d939c,#b4b9c0 45%,#9197a0 75%,#767c86)}
.enquiry-shade{left:0;top:2320px;width:1200px;height:722px;background:rgba(70,76,88,.35)}
.accordion{left:111px;top:2449px;width:526px;height:480px;background:var(--white)}
.acc-item{left:111px;width:526px;height:79px;background:var(--white);box-shadow:0 4px 8px rgba(0,0,0,.1);display:flex;align-items:center;padding-left:14px}
.acc-num{width:52px;height:52px;border-radius:50%;background:var(--blue);color:var(--white);font-weight:700;font-size:21px;display:flex;align-items:center;justify-content:center}
.acc-title{font-size:22px;font-weight:600;color:var(--ink);margin-left:13px;flex:1}
.acc-sign{color:var(--blue);font-size:30px;font-weight:700;margin-right:32px}
.acc-body{left:147px;top:2737px;width:454px;height:158px;background:var(--white);box-shadow:0 2px 12px rgba(0,0,0,.12);padding:40px 42px 0;font-size:15.5px;line-height:30px}
.enq-title{right:114px;top:2440px;font-size:38px;font-weight:700;color:var(--white)}
.enq-lines{right:112px;top:2575px;text-align:right;font-size:36px;font-weight:700;color:var(--white);line-height:61px}
/* footer */
.footer{left:0;top:3042px;width:1200px;height:288px;background:var(--footer);color:var(--white)}
.footer-base{left:0;top:3330px;width:1200px;height:47px;background:var(--footer-deep);color:var(--white);font-size:15px;display:flex;align-items:center;padding-left:111px}
.social{top:3067px;width:16px;height:16px;border-radius:50%;background:var(--white)}
.footer-brand{left:107px;top:3104px;color:var(--white);font-weight:700;display:flex;gap:10px;align-items:flex-start}
.footer-brand .brand-name{font-size:40px;line-height:44px}
.footer-brand .brand-tag{font-size:10px;line-height:12px}
.footer-brand .brand-mark{width:18px;height:18px;margin-top:14px}
.fnav{top:3115px;font-size:15px;font-weight:600;text-transform:uppercase;color:var(--white)}
.fcopy{top:3214px;font-size:15.5px;line-height:30px;color:var(--white)}
</style>
</head>
<body>

<!-- header -->
<header class="abs site-header"></header>
<div class="abs brand">
  <div class="brand-mark"></div>
  <div><div class="brand-name">Corvantek</div><div class="brand-tag">Aluminium Windows &amp; Doors</div></div>
</div>
<div class="abs header-rule"></div>
<nav>
  <div class="abs nav nav-active">Home</div>
  <div class="abs nav" style="left:562px">About Us</div>
  <div class="abs nav" style="left:688px">Products</div>
  <div class="abs nav" style="left:821px">Make&nbsp;&nbsp;An Enquiry</div>
  <div class="abs nav" style="left:1016px">Contact</div>
</nav>

<!-- hero -->
<div class="abs hero-photo" role="img" aria-label="Gloved workers handling a large sheet of glass"></div>
<div class="abs thumb-strip"></div>
<div class="abs thumb" style="left:821px;background:linear-gradient(135deg,#5a9bc8,#d7ecf5 50%,#3d78a8)" role="img" aria-label="Close-up of blue glass panes"></div>
<div class="abs thumb" style="left:915px;background:linear-gradient(135deg,#1f6b3d,#2fa35e 50%,#7a2d22)" role="img" aria-label="Stacked green glass edges"></div>
<div class="abs thumb" style="left:1009px;background:linear-gradient(135deg,#e8d3b8,#c98d63 50%,#9fc7c2)" role="img" aria-label="Hand holding a glass sample"></div>
<div class="abs thumb" style="left:1104px;background:linear-gradient(135deg,#0f2a2a,#1f5e55 55%,#0c1d1e)" role="img" aria-label="Dark green glass sheets"></div>

<div class="abs slide-no slide-on">1</div>
<div class="abs slide-no" style="left:35px;top:356px">2</div>
<div class="abs slide-no" style="left:35px;top:392px">3</div>

<h1 class="abs hero-title">BULLET RESISTANT<br><span>WINDOW &amp; DOORS</span></h1>
<div class="abs hero-sub">YOUR FIRST LINE OF DEFENCE</div>
<p class="abs hero-copy">Lorem ipsum dolor sit amet, consectetur adipi-scing elit, sed do eiusmod tempor incididunt ut labore et dolore magna aliqua. Ut enim ad minima veniam, quis nostrum exercitationem ullam corporis suscipit consequatur</p>
<div class="btn" style="left:111px;top:520px;width:141px;height:41px">Get Started</div>

<!-- features -->
<div class="abs feature-band"></div>
<div class="abs feature-frame"></div>
<div class="abs feature" style="left:275px">
  <svg width="64" height="64" viewBox="0 0 64 64" fill="none" stroke="var(--blue)" stroke-width="2.2" stroke-linejoin="round"><path d="M32 6l16 6v13c0 10-7 17-16 20-9-3-16-10-16-20V12z"/><path d="M25 25l5 5 9-10"/><path d="M6 40l10 12h12M58 40L48 52H36"/></svg>
  <h3>Premium Protection</h3>
  <p>Lorem ipsum dolor sit amet, consectetur</p>
</div>
<div class="abs feature" style="left:498px">
  <svg width="64" height="64" viewBox="0 0 64 64" fill="none" stroke="var(--blue)" stroke-width="2.2"><circle cx="32" cy="32" r="7"/><circle cx="32" cy="12" r="5"/><circle cx="32" cy="52" r="5"/><circle cx="13" cy="22" r="5"/><circle cx="51" cy="22" r="5"/><circle cx="13" cy="42" r="5"/><circle cx="51" cy="42" r="5"/><circle cx="8" cy="32" r="3"/><circle cx="56" cy="32" r="3"/></svg>
  <h3>Aesthetically<br>Designed</h3>
  <p style="margin-top:0">Lorem ipsum dolor sit amet, consectetur</p>
</div>
<div class="abs feature" style="left:721px">
  <svg width="64" height="64" viewBox="0 0 64 64" fill="none" stroke="var(--blue)" stroke-width="2.2"><circle cx="32" cy="32" r="7"/><circle cx="32" cy="12" r="5"/><circle cx="32" cy="52" r="5"/><circle cx="13" cy="22" r="5"/><circle cx="51" cy="22" r="5"/><circle cx="13" cy="42" r="5"/><circle cx="51" cy="42" r="5"/><circle cx="8" cy="32" r="3"/><circle cx="56" cy="32" r="3"/></svg>
  <h3>Promptly Delivered</h3>
  <p>Lorem ipsum dolor sit amet, consectetur</p>
</div>

<!-- about -->
<section class="abs about"></section>
<div class="abs block" style="left:368px;top:1097px;width:105px;height:49px"></div>
<div class="abs block" style="left:205px;top:1374px;width:82px;height:51px"></div>
<div class="abs" style="left:111px;top:1050px;width:257px;height:324px;background:linear-gradient(135deg,#f4f4f2,#d9dcd8 40%,#7d9b5c 75%,#c9d7b8)" role="img" aria-label="White window frame open to garden greenery"></div>
<div class="abs" style="left:287px;top:1146px;width:257px;height:324px;background:linear-gradient(135deg,#e6ecec,#9fd3c8 45%,#2f9c8a 65%,#cfe4e1);box-shadow:0 4px 14px rgba(0,0,0,.15)" role="img" aria-label="Gloved hand holding thick layered glass panels"></div>
<h2 class="abs" style="left:590px;top:1058px">ABOUT US</h2>
<p class="abs about-copy">Sed ut perspiciatis unde omnis iste natus error sit vo-luptatem accusantium doloremque laudantium, totam rem aperiam, eaque ipsa quae ab illo inventore veritatis et quasi architecto beatae vitae dicta sunt explicabo. Nemo enim ipsam voluptatem quia voluptas sit aspernatur aut odit aut fugit, sed quia consequuntur magni dolores eos qui ratione voluptatem sequi nesciunt. Neque porro quisquam est,</p>
<div class="btn" style="left:590px;top:1375px;width:140px;height:42px">Read More</div>

<!-- range -->
<section class="range">
  <h2 class="abs" style="left:0;top:1645px;width:1200px;text-align:center">SUPERIOR PROTECTION, SLEEK DESIGN</h2>
</section>
<div class="abs range-img" style="left:111px;background:linear-gradient(90deg,#e8ecef,#b8c2cb 40%,#dfe4e8 70%,#a9b4bd)" role="img" aria-label="Row of white sliding window frames"></div>
<div class="abs range-img" style="left:454px;background:linear-gradient(90deg,#9aa5ad,#dfe8ee 40%,#f4efe6 75%,#e6ddd0)" role="img" aria-label="Open glass door onto a bright balcony with curtain"></div>
<div class="abs range-img" style="left:794px;background:linear-gradient(135deg,#2e6fb8,#a7cbec 40%,#3b7dc4 70%,#d5e6f5)" role="img" aria-label="Glass office tower reflecting blue sky"></div>
<div class="abs range-box" style="left:111px"><h3>LOREM IPSUM</h3><p>inventore veritatis et quasi<br>architecto beatae vitae</p></div>
<div class="abs range-box" style="left:454px"><h3>LOREM IPSUM</h3><p>inventore veritatis et quasi<br>architecto beatae vitae</p></div>
<div class="abs range-box" style="left:794px"><h3>LOREM IPSUM</h3><p>inventore veritatis et quasi<br>architecto beatae vitae</p></div>
<div class="btn" style="left:189px;top:2175px;width:140px;height:41px">Read More</div>
<div class="btn" style="left:532px;top:2175px;width:140px;height:41px">Read More</div>
<div class="btn" style="left:866px;top:2175px;width:140px;height:41px">Read More</div>

<!-- enquiry -->
<section class="abs enquiry" role="img" aria-label="Workshop stacked with new window frames"></section>
<div class="abs enquiry-shade"></div>
<div class="abs accordion"></div>
<div class="abs acc-item" style="top:2449px"><div class="acc-num">01</div><div class="acc-title">Explore Our Range</div><div class="acc-sign">+</div></div>
<div class="abs acc-item" style="top:2543px"><div class="acc-num">02</div><div class="acc-title">Make An Enquiry</div><div class="acc-sign">+</div></div>
<div class="abs acc-item" style="top:2638px"><div class="acc-num">03</div><div class="acc-title">Receive Customised Quote</div><div class="acc-sign">&minus;</div></div>
<p class="abs acc-body">Sed ut perspiciatis unde omnis iste natus error sit voluptatem accusantium doloremque lau-dantium, totam rem aperiam, eaque ipsa quae</p>
<h2 class="abs enq-title">MAKE AN ENQUIRY</h2>
<div class="abs enq-lines">Premium Protection<br>Aesthetically Designed<br>Promptly Delivered</div>
<div class="btn" style="left:899px;top:2888px;width:190px;height:42px;text-transform:none;font-size:15px;font-weight:600">Make an Enquiry</div>

<!-- footer -->
<footer class="abs footer"></footer>
<div class="abs social" style="left:888px"></div>
<div class="abs social" style="left:932px"></div>
<div class="abs social" style="left:967px"></div>
<div class="abs social" style="left:1015px"></div>
<div class="abs social" style="left:1064px"></div>
<div class="abs footer-brand">
  <div class="brand-mark"></div>
  <div><div class="brand-name">Corvantek</div><div class="brand-tag">ALUMINIUM WINDOWS &amp; DOORS</div></div>
</div>
<div class="abs fnav" style="left:463px">Home</div>
<div class="abs fnav" style="left:558px">About Us</div>
<div class="abs fnav" style="left:684px">Products</div>
<div class="abs fnav" style="left:818px">Make&nbsp;&nbsp;An Enquiry</div>
<div class="abs fnav" style="left:1012px">Contact</div>
<p class="abs fcopy" style="left:111px;width:296px;text-align:justify">Lorem ipsum dolor sit amet, consecte-tur adipiscing elit, sed do eiusmod tempor</p>
<svg class="abs" style="left:522px;top:3221px" width="13" height="17" viewBox="0 0 13 17"><path d="M6.5 0a6.5 6.5 0 0 0-6.5 6.5C0 11 6.5 17 6.5 17S13 11 13 6.5A6.5 6.5 0 0 0 6.5 0z" fill="var(--blue)"/><circle cx="6.5" cy="6.5" r="2.4" fill="var(--footer)"/></svg>
<p class="abs fcopy" style="left:546px">42 Harbourline<br>Street Sydney, NSW 2010 AU</p>
<svg class="abs" style="left:865px;top:3222px" width="16" height="16" viewBox="0 0 16 16"><path d="M3 1l3 3-1.6 2.2a9 9 0 0 0 5.4 5.4L12 10l3 3-2 2.2C7 15 1 9 .8 3z" fill="var(--blue)"/></svg>
<svg class="abs" style="left:864px;top:3254px" width="18" height="13" viewBox="0 0 18 13"><rect width="18" height="13" rx="1" fill="var(--blue)"/><path d="M1 1l8 6 8-6" fill="none" stroke="var(--footer)" stroke-width="1.3"/></svg>
<p class="abs fcopy" style="left:893px">+61 2 5550 1234<br>info@corvantek.com</p>
<div class="abs footer-base">&copy; 2023&nbsp; Corvantek</div>

</body>
</html>
```